Business Card for New Convenience Store

We need a business card for our new convenience store using our logo. We want to have a color scheme and back ground created that will be transferable to other media platforms and advertising.

Industry/Entity Type

Convenience Store

```html
<!DOCTYPE html>
<html lang="en">
<head>
<meta charset="utf-8">
<title>Cedar Stop – Business Card</title>
<link href="https://fonts.googleapis.com/css2?family=Questrial&display=swap" rel="stylesheet">
<style>
  :root {
    --brand-red: #e3141f;
    --brand-red-dark: #c10e18;
    --card-white: #ffffff;
    --card-mist: #eeeeee;
    --name-grey: #8c8c8c;
    --text-dark: #2a2a2a;
    --rule-grey: #b9b9bf;
    --page-bg: #e6e4e0;
    --photo-sky: #dfe6ea;
    --photo-brick: #8a5a3c;
    --photo-ground: #cfcac4;
  }
  * { box-sizing: border-box; margin: 0; padding: 0; }
  html, body {
    width: 1200px; height: 800px; overflow: hidden;
    background: var(--page-bg);
    font-family: "Questrial", sans-serif;
  }
  .canvas {
    position: relative; width: 1200px; height: 800px;
    display: flex; align-items: center; justify-content: center; gap: 50px;
  }
  .card {
    position: relative; width: 525px; height: 300px;
    overflow: hidden;
    box-shadow: 0 6px 18px rgba(0,0,0,.18);
  }

  /* Front */
  .card-front {
    background: var(--brand-red);
    padding: 22px;
  }
  .card-front .panel {
    position: relative; width: 100%; height: 100%;
    background: linear-gradient(135deg, var(--card-white) 40%, var(--card-mist));
    padding: 28px 26px;
  }
  .holder-name {
    font-size: 40px; font-weight: 400; letter-spacing: 3px; line-height: 1;
    color: var(--name-grey); text-transform: uppercase;
    white-space: nowrap;
  }
  .contact {
    position: absolute; left: 140px; top: 96px;
    padding-left: 16px;
    border-left: 6px solid var(--rule-grey);
    font-style: normal;
    font-size: 19px; line-height: 1.15; color: var(--text-dark);
  }
  .contact .role { color: var(--name-grey); }

  /* Back */
  .card-back { background: var(--card-white); }
  .band-top {
    position: absolute; left: 0; top: 14px; width: 100%; height: 30px;
    background: var(--brand-red);
  }
  .storefront {
    position: absolute; left: 0; top: 44px; width: 100%; height: 196px;
    background: linear-gradient(180deg, var(--photo-sky) 0%, #e9ecee 30%, var(--photo-brick) 62%, var(--photo-ground) 100%);
  }
  .store-name {
    position: absolute; right: 48px; top: 120px;
    font-size: 30px; color: var(--card-white); letter-spacing: 1px;
    display: flex; align-items: center; gap: 10px;
  }
  .store-name .dot {
    width: 14px; height: 14px; border-radius: 50%; background: var(--card-white);
  }
  .band-bottom { position: absolute; left: 0; bottom: 0; width: 100%; height: 80px; }
</style>
</head>
<body>
<main class="canvas">

  <section class="card card-front" aria-label="Business card front">
    <div class="panel">
      <h1 class="holder-name">Dana Whitfield</h1>
      <address class="contact">
        <span class="role">Manager</span><br>
        205-555-0148<br>
        dwhitfield@cedarstop.com<br>
        412 Cedar Bend Dr.<br>
        Larkspur, AL 36010
      </address>
    </div>
  </section>

  <section class="card card-back" aria-label="Business card back">
    <div class="band-top"></div>
    <div class="storefront" role="img" aria-label="Photo of the new store building with stone and glass facade and shoppers walking in"></div>
    <div class="store-name"><span class="dot"></span>Cedar Stop</div>
    <svg class="band-bottom" viewBox="0 0 525 80" preserveAspectRatio="none" aria-hidden="true">
      <polygon points="0,0 525,0 525,60 0,60" fill="var(--brand-red)"/>
      <polygon points="0,0 200,0 120,60 0,60" fill="var(--brand-red-dark)"/>
      <rect x="0" y="60" width="525" height="20" fill="var(--card-white)"/>
    </svg>
  </section>

</main>
</body>
</html>
```